IT COMPANYcutting edge tec business card

we are IT company that building any apps.
we need business card in japanese and english
You don’t have to include all information in front one you can attach part of that information to back-side
company name : 株式会社ひかりの丘 (BRIGHTHILL Inc.)
concept : cutting-edge technology
role : 取締役 (director)
name : 呉 炫秀 (Oh Hyeonsuk)
post number : 154-0038
address : 東京都世田谷区西若葉台5-14-8 (5-14-8, Nishiwakabadai, Setagaya Ku, Tokyo To, 154-0038, Japan)
Tel:+81-3-5917-2846
Mobile:+81-80-7253-3169
Email : hoh@brighthill-lab.com
website : www.brighthill-lab.com

we dont have logo so please make it as well
we also looking for designer who can make homapage design.

Contact Information for Business Card

cutting-edge design and modern for IT

Font styles to use
Sans Serif

Colors
34a6d7
33b8a4
6092c4
3377b5
886aae
6b449b
b868aa
a64599

Requirements
Must have
• Simple but designed

```html
<!DOCTYPE html>
<html lang="ja">
<head>
<meta charset="utf-8">
<title>BRIGHTHILL Inc. — Identity &amp; Business Card</title>
<link rel="stylesheet" href="https://fonts.googleapis.com/css2?family=Open+Sans:wght@400;600&family=Noto+Sans+JP:wght@400;500&display=swap">
<style>
  :root {
    --brand-blue: #34a6d7;
    --brand-deep: #3377b5;
    --ink: #1a1a1a;
    --card-dark: #000000;
    --card-light: #ffffff;
    --page: #ffffff;
    --rule: #34a6d7;
    --shadow: rgba(0,0,0,0.45);
  }
  html, body {
    margin: 0;
    padding: 0;
    width: 1200px;
    height: 1200px;
    overflow: hidden;
    background: var(--page);
  }
  .sheet {
    position: relative;
    width: 1200px;
    height: 1200px;
    font-family: "Open Sans", "Noto Sans JP", sans-serif;
  }

  /* ---------- logo lockup ---------- */
  .lockup {
    position: absolute;
    display: flex;
    align-items: center;
    gap: 16px;
    color: var(--brand-blue);
  }
  .lockup__mark {
    flex: none;
    background: var(--brand-blue);
  }
  .lockup__names {
    display: flex;
    flex-direction: column;
    line-height: 1;
    font-weight: 400;
  }
  .lockup__en {
    font-family: "Open Sans", sans-serif;
    letter-spacing: 0.01em;
    white-space: nowrap;
  }
  .lockup__jp {
    font-family: "Noto Sans JP", sans-serif;
    white-space: nowrap;
  }

  .lockup--hero { left: 110px; top: 108px; }
  .lockup--hero .lockup__mark { width: 86px; height: 86px; }
  .lockup--hero .lockup__en { font-size: 50px; }
  .lockup--hero .lockup__jp { font-size: 36px; margin-top: 10px; }

  .dark-panel {
    position: absolute;
    left: 608px; top: 70px;
    width: 504px; height: 181px;
    background: var(--card-dark);
  }
  .lockup--panel { left: 634px; top: 112px; }
  .lockup--panel .lockup__mark { width: 80px; height: 80px; }
  .lockup--panel .lockup__en { font-size: 46px; }
  .lockup--panel .lockup__jp { font-size: 33px; margin-top: 10px; }

  /* ---------- cards ---------- */
  .card {
    position: absolute;
    overflow: hidden;
    box-shadow: 14px 18px 22px var(--shadow);
  }
  .card__texture {
    position: absolute;
    inset: 0;
  }
  .card--front {
    left: 293px; top: 336px;
    width: 584px; height: 325px;
    background: var(--card-dark);
  }
  .card--front .card__texture {
    background: radial-gradient(ellipse at 55% 45%, #0b1a24 0%, #050a0e 55%, #000 100%);
  }
  .lockup--front { left: 136px; top: 128px; gap: 12px; }
  .lockup--front .lockup__mark { width: 58px; height: 58px; }
  .lockup--front .lockup__en { font-size: 33px; }
  .lockup--front .lockup__jp { font-size: 24px; margin-top: 7px; }

  .card--back {
    left: 293px; top: 750px;
    width: 591px; height: 329px;
    background: var(--card-light);
  }
  .card--back .card__texture {
    background: linear-gradient(135deg, #f6fbfe 0%, #ffffff 50%, #f3f9fd 100%);
  }
  .lockup--back { left: 28px; top: 142px; gap: 9px; }
  .lockup--back .lockup__mark { width: 40px; height: 40px; }
  .lockup--back .lockup__en { font-size: 22px; }
  .lockup--back .lockup__jp { font-size: 17px; margin-top: 5px; }

  .card__divider {
    position: absolute;
    left: 274px; top: 31px;
    width: 1.5px; height: 269px;
    background: var(--rule);
  }
  .person {
    position: absolute;
    left: 312px; top: 44px;
    color: var(--brand-deep);
  }
  .person__name {
    font-family: "Noto Sans JP", sans-serif;
    font-size: 34px;
    font-weight: 400;
    letter-spacing: 0.12em;
    line-height: 1;
    margin: 0;
  }
  .person__role {
    font-family: "Noto Sans JP", sans-serif;
    font-size: 14px;
    color: var(--brand-blue);
    margin: 8px 0 0;
  }
  .contacts {
    position: absolute;
    left: 304px; top: 114px;
    margin: 0; padding: 0;
    list-style: none;
    font-family: "Noto Sans JP", "Open Sans", sans-serif;
    color: var(--ink);
  }
  .contact {
    display: flex;
    align-items: center;
    height: 34px;
  }
  .contact__icon {
    flex: none;
    width: 27px; height: 27px;
    margin-right: 20px;
  }
  .contact__text { font-size: 10.5px; line-height: 1.2; }
  .contact__text--main { font-size: 11px; }
  .contact__address-jp { display: block; font-size: 11.5px; }
  .contact__address-en { display: block; font-size: 7px; margin-top: 2px; }
</style>
</head>
<body>
<main class="sheet">

  <!-- primary logo on white -->
  <div class="lockup lockup--hero">
    <span class="lockup__mark"></span>
    <span class="lockup__names">
      <span class="lockup__en">BRIGHTHILL Inc.</span>
      <span class="lockup__jp">株式会社ひかりの丘</span>
    </span>
  </div>

  <!-- reversed logo on black -->
  <div class="dark-panel"></div>
  <div class="lockup lockup--panel">
    <span class="lockup__mark"></span>
    <span class="lockup__names">
      <span class="lockup__en">BRIGHTHILL Inc.</span>
      <span class="lockup__jp">株式会社ひかりの丘</span>
    </span>
  </div>

  <!-- card front -->
  <section class="card card--front">
    <div class="card__texture" role="img" aria-label="Faint dark-blue hexagonal grid pattern on black"></div>
    <div class="lockup lockup--front">
      <span class="lockup__mark"></span>
      <span class="lockup__names">
        <span class="lockup__en">BRIGHTHILL Inc.</span>
        <span class="lockup__jp">株式会社ひかりの丘</span>
      </span>
    </div>
  </section>

  <!-- card back -->
  <section class="card card--back">
    <div class="card__texture" role="img" aria-label="Very light blue hexagonal grid pattern on white"></div>
    <div class="lockup lockup--back">
      <span class="lockup__mark"></span>
      <span class="lockup__names">
        <span class="lockup__en">BRIGHTHILL Inc.</span>
        <span class="lockup__jp">株式会社ひかりの丘</span>
      </span>
    </div>

    <div class="card__divider"></div>

    <div class="person">
      <p class="person__name">呉 炫 秀</p>
      <p class="person__role">取締役 (Director)</p>
    </div>

    <ul class="contacts">
      <li class="contact">
        <svg class="contact__icon" viewBox="0 0 28 28" aria-hidden="true">
          <circle cx="14" cy="14" r="14" fill="#000"/>
          <path d="M14 5.5c-3.4 0-6 2.6-6 5.9 0 4.3 6 10.8 6 10.8s6-6.5 6-10.8c0-3.3-2.6-5.9-6-5.9z" fill="#fff"/>
          <circle cx="14" cy="11.3" r="2.3" fill="none" stroke="#000" stroke-width="1"/>
        </svg>
        <span class="contact__text">
          <span class="contact__address-jp">東京都世田谷区西若葉台5-14-8</span>
          <span class="contact__address-en">(5-14-8, Nishiwakabadai, Setagaya Ku, Tokyo To,<br>154-0038, Japan)</span>
        </span>
      </li>
      <li class="contact">
        <svg class="contact__icon" viewBox="0 0 28 28" aria-hidden="true">
          <circle cx="14" cy="14" r="14" fill="#000"/>
          <path d="M9 7.5l2.6-.6 1.6 3.6-1.8 1.3c.8 1.8 2.2 3.2 4 4l1.3-1.8 3.6 1.6-.6 2.6c-.2.7-.8 1.1-1.5 1-5.2-.6-9.3-4.7-9.9-9.9-.1-.7.3-1.3 1-1.5z" fill="#fff"/>
          <path d="M15.5 8.2a4.5 4.5 0 0 1 4.3 4.3M15.5 5.8a6.9 6.9 0 0 1 6.7 6.7" fill="none" stroke="#fff" stroke-width="1.1"/>
        </svg>
        <span class="contact__text contact__text--main">+81 3 5917 2846</span>
      </li>
      <li class="contact">
        <svg class="contact__icon" viewBox="0 0 28 28" aria-hidden="true">
          <circle cx="14" cy="14" r="14" fill="#000"/>
          <rect x="9.5" y="6" width="9" height="16" rx="1.5" fill="none" stroke="#fff" stroke-width="1.6"/>
          <rect x="11" y="8" width="6" height="10" fill="#fff"/>
          <circle cx="14" cy="20" r="0.9" fill="#fff"/>
        </svg>
        <span class="contact__text contact__text--main">+81 80 7253 3169</span>
      </li>
      <li class="contact">
        <svg class="contact__icon" viewBox="0 0 28 28" aria-hidden="true">
          <circle cx="14" cy="14" r="14" fill="#000"/>
          <rect x="7" y="9" width="14" height="10" fill="#fff"/>
          <path d="M7 9l7 5.5L21 9M7 19l5-4.5M21 19l-5-4.5" fill="none" stroke="#000" stroke-width="0.8"/>
        </svg>
        <span class="contact__text contact__text--main">hoh@brighthill-lab.com</span>
      </li>
      <li class="contact">
        <svg class="contact__icon" viewBox="0 0 28 28" aria-hidden="true">
          <circle cx="14" cy="14" r="14" fill="#000"/>
          <g fill="none" stroke="#fff" stroke-width="1">
            <circle cx="14" cy="14" r="7.5"/>
            <ellipse cx="14" cy="14" rx="3.3" ry="7.5"/>
            <path d="M6.5 14h15M7.5 10.5h13M7.5 17.5h13M14 6.5v15"/>
          </g>
        </svg>
        <span class="contact__text contact__text--main">www.brighthill-lab.com</span>
      </li>
    </ul>
  </section>

</main>
</body>
</html>
```